Design for web based travel expence program

We need a design template for a web based travel expence program we have created. The current design is based on a standard framework, and it needs to be "spiced" up.
Please notice that there are only 3-4 screen shots that needs an "upspice" of the design. No complete web design is expected for this price. For the right designer we have many more jobs coming up!
Tovalin Accounting is a Scandinavian accounting company with offices in Norway (Oslo) and Stockholm (Sweden). Our goal is to be a proactive accounting company known for trouble-free solutions and wide knowledge about what we do. We have created an "easy" accounting program enabling clients to take picture of vouchers, upload them to our portal and gather them to a travel expense scheme that can be approved and sent directly into an accounting program.
The program is pure web based and created with sophisticated programming code, but only with a standard framework as design template. We need a touch of professional design that easily can be implemented “on top” of the framework.
We are thinking that the designer should add icons and create the squared elements a bit rounder and with a more beautiful touch.
We are looking for a designer that preferably can create CSS files with an improved design, though the first step should be to create some pictures/Photshop examples on how it could look like. The files we have uploaded are the screen shots that needs to be improved with a better design.
Reason: Thank you for the designs, but still a bit few to choose between.
Target Market(s)
All type of businesses, but the end user is in focus. The program is designed to be easy-to-learn and very useful for all persons dealing with travel expence forms.
Industry/Entity Type
Accounting

```html
<!DOCTYPE html>
<html lang="no">
<head>
<meta charset="utf-8">
<title>Utleggjuni – Lag refusion</title>
<link href="https://fonts.googleapis.com/css2?family=Ubuntu:wght@400;500;700&display=swap" rel="stylesheet">
<style>
:root{
  --sidebar:#1c1f29;
  --nav-active:#33a6dc;
  --nav-light:#8fd2f1;
  --bg:#f1f1f1;
  --panel:#ffffff;
  --line:#dedede;
  --text:#333a40;
  --muted:#9a9a9a;
  --blue:#2ea8e0;
  --blue-light:#8fd4f2;
  --dark:#3a4150;
  --orange:#f1a437;
  --orange-border:#d98b1f;
  --card:#f5f5f5;
}
*{box-sizing:border-box;margin:0;padding:0}
html,body{width:1200px;height:971px;overflow:hidden}
body{font-family:"Ubuntu",sans-serif;background:var(--bg);color:var(--text);position:relative;font-size:13px}
.sidebar{position:absolute;left:0;top:0;width:214px;height:971px;background:var(--sidebar)}
.side-item{position:absolute;left:0;width:214px;height:32px;display:flex;align-items:center;padding-left:30px;color:#fff;font-size:14px;gap:9px}
.side-item.refund{top:110px;background:var(--nav-active)}
.side-item.receipts{top:142px;background:var(--nav-light)}
.badge{position:absolute;right:10px;top:8px;width:23px;height:17px;border:1px solid #fff;border-radius:4px;background:#fff;color:#888;font-size:11px;text-align:center;line-height:15px}
.panel{position:absolute;left:234px;top:17px;width:943px;height:907px;background:var(--panel);border:1px solid var(--line);border-radius:3px}
.header{position:absolute;left:0;top:0;width:100%;height:62px;border-bottom:1px solid var(--line)}
.divider{position:absolute;left:210px;top:62px;bottom:0;width:1px;background:var(--line)}
.btn{position:absolute;display:flex;align-items:center;justify-content:center;border-radius:3px;font-size:13px;color:#fff;border:1px solid transparent}
.btn-orange{background:linear-gradient(#f5b14c,#ee9c2b);border-color:var(--orange-border)}
.btn-blue{background:linear-gradient(#3fb4e8,#2a9fd8);border-color:#2590c6}
.btn-dark{background:linear-gradient(#465061,#333a47);border-color:#2a303b}
.btn-white{background:#fff;border-color:#d6d6d6;color:#555}
.title{position:absolute;left:237px;top:22px;font-size:18px;font-weight:700;color:#2d3136}
.status{position:absolute;right:18px;top:22px;font-size:18px;color:var(--muted)}
.crumb{position:absolute;left:238px;top:78px;font-size:13px}
.crumb a{color:var(--blue);text-decoration:none}
.name-input{position:absolute;left:238px;top:104px;width:492px;height:35px;border:1px solid #d4d4d4;border-radius:4px;padding-left:16px;line-height:33px;font-size:13px}
.card{position:absolute;background:linear-gradient(#fff,var(--card));border:1px solid #e6e6e6;border-radius:4px}
.card h2{font-weight:400;font-size:17px;margin:15px 0 0 18px}
.kv{left:238px;top:173px;width:334px;height:115px}
.kv p{margin-left:18px;font-size:13px}
.reise{left:238px;top:299px;width:334px;height:445px;background:var(--card)}
.reise label{position:absolute;left:18px;font-size:13px}
.field{position:absolute;left:17px;width:318px;background:#fff;border:1px solid #d2d2d2;border-radius:5px;font-size:12px;color:#777;padding-left:14px;display:flex;align-items:center}
.field .arrow{position:absolute;right:12px;top:50%;margin-top:-3px;border:5px solid transparent;border-top:7px solid #777;border-bottom:0}
.ledige{left:588px;top:173px;width:334px;height:568px;background:var(--card)}
.tile{position:absolute;width:143px;height:110px;background:#fff;border:1px solid #dadada;border-radius:4px;overflow:hidden}
.tile-head{height:28px;background:var(--blue-light);font-size:12px;padding-left:15px;line-height:28px;color:#2d3136}
.tile.selected .tile-head{background:var(--blue);color:#dff3fd}
.tile-row{display:flex;align-items:center;gap:8px;font-size:12px;margin:0 0 0 15px;height:26px}
.tile-row:first-of-type{margin-top:2px}
</style>
</head>
<body>
<nav class="sidebar">
  <div class="side-item refund">
    <svg width="18" height="15" viewBox="0 0 18 15"><rect x="1" y="1" width="16" height="13" fill="none" stroke="#fff" stroke-width="1.5"/><rect x="4" y="6" width="4" height="5" fill="#fff"/><path d="M10 6h5M10 9h5M4 3.5h11" stroke="#fff"/></svg>
    Refusjoner
  </div>
  <div class="side-item receipts">
    <svg width="18" height="18" viewBox="0 0 18 18"><circle cx="9" cy="9" r="7.5" fill="none" stroke="#fff" stroke-width="1.5"/><path d="M9 4.5v7M5.8 8.5 9 11.8l3.2-3.3" fill="none" stroke="#fff" stroke-width="1.6"/></svg>
    Kvitteringer
    <span class="badge">1</span>
  </div>
</nav>

<main class="panel">
  <header class="header">
    <div class="btn btn-orange" style="left:21px;top:19px;width:172px;height:29px">
      <svg width="8" height="9" viewBox="0 0 8 9" style="margin-right:7px"><path d="M6 1 2 4.5 6 8z" fill="#fff"/></svg>Lagre og tilbake
    </div>
    <div class="title">UTLEGGJUNI</div>
    <div class="status">Status: ikke sendt</div>
  </header>
  <div class="divider"></div>

  <div class="btn btn-blue" style="left:21px;top:151px;width:172px;height:29px">Kvitteringer</div>
  <div class="btn btn-dark" style="left:21px;top:188px;width:172px;height:29px">Reiseregning</div>
  <div class="btn btn-white" style="left:21px;top:224px;width:172px;height:30px">Reiseregning</div>

  <div class="crumb">Lag refusion &nbsp;/&nbsp; <a>Send</a></div>
  <div class="name-input">Utleggjuni</div>

  <section class="card kv">
    <h2>Kvitteringer</h2>
    <p style="margin-top:9px">Antall : 3</p>
    <p style="margin-top:10px">Belop : 804</p>
    <div class="btn btn-blue" style="left:203px;top:48px;width:132px;height:30px">Velg kvitteringer</div>
  </section>

  <section class="card reise">
    <h2>Reise</h2>
    <label style="top:50px">Formal</label>
    <div class="field" style="top:70px;height:64px"></div>
    <label style="top:146px">Destination</label>
    <div class="field" style="top:166px;height:37px"></div>
    <label style="top:216px">Fra</label>
    <div class="field" style="top:236px;height:37px">mm/dd/yyyy<span class="arrow"></span></div>
    <label style="top:282px">Til</label>
    <div class="field" style="top:302px;height:37px">mm/dd/yyyy<span class="arrow"></span></div>
    <label style="top:352px;color:var(--blue);font-size:14px">States satser</label>
    <label style="top:373px">Belop:0</label>
    <div class="btn btn-orange" style="left:19px;top:407px;width:153px;height:30px">Beregn automatisk</div>
    <div class="btn btn-orange" style="left:178px;top:407px;width:102px;height:30px">Velg saster</div>
  </section>

  <div class="btn btn-blue" style="left:258px;top:753px;width:53px;height:28px">Slett</div>
  <div class="btn btn-dark" style="left:317px;top:753px;width:156px;height:28px">Forhandsvis og send</div>

  <section class="card ledige">
    <h2>Ledige kvitteringer</h2>
  </section>
</main>

<svg width="0" height="0" style="position:absolute">
  <symbol id="i-cal" viewBox="0 0 12 12"><rect x="1" y="2" width="10" height="9" fill="none" stroke="#8a3a3a"/><path d="M1 4.5h10M4 5v6M7 5v6M1 7.5h10" stroke="#8a3a3a" stroke-width=".7"/><path d="M3.5 1v2M8.5 1v2" stroke="#8a3a3a"/></symbol>
  <symbol id="i-cash" viewBox="0 0 12 12"><rect x=".5" y="3" width="11" height="6" fill="none" stroke="#333"/><circle cx="6" cy="6" r="1.6" fill="#333"/></symbol>
  <symbol id="i-doc" viewBox="0 0 12 12"><path d="M3 1h4l2.5 2.5V11H3z" fill="none" stroke="#555"/><path d="M4.5 6h3.5M4.5 8h3.5" stroke="#c44"/></symbol>
</svg>

<div style="position:absolute;left:0;top:0">
  <!-- receipt tiles -->
  <div class="tile" style="left:841px;top:238px"><div class="tile-head">Elektronikk</div><div class="tile-row"><svg width="12" height="12"><use href="#i-cal"/></svg>2013-03-08</div><div class="tile-row"><svg width="12" height="12"><use href="#i-cash"/></svg>100</div><div class="tile-row"><svg width="12" height="12"><use href="#i-doc"/></svg>1</div></div>
  <div class="tile" style="left:995px;top:238px"><div class="tile-head">Elektronikk</div><div class="tile-row"><svg width="12" height="12"><use href="#i-cal"/></svg>2013-03-08</div><div class="tile-row"><svg width="12" height="12"><use href="#i-cash"/></svg>100</div><div class="tile-row"><svg width="12" height="12"><use href="#i-doc"/></svg>1</div></div>
  <div class="tile" style="left:841px;top:358px"><div class="tile-head">Elektronikk</div><div class="tile-row"><svg width="12" height="12"><use href="#i-cal"/></svg>2013-03-08</div><div class="tile-row"><svg width="12" height="12"><use href="#i-cash"/></svg>100</div><div class="tile-row"><svg width="12" height="12"><use href="#i-doc"/></svg>1</div></div>
  <div class="tile selected" style="left:995px;top:358px"><div class="tile-head">Elektronikk</div><div class="tile-row"><svg width="12" height="12"><use href="#i-cal"/></svg>2013-03-08</div><div class="tile-row"><svg width="12" height="12"><use href="#i-cash"/></svg>100</div><div class="tile-row"><svg width="12" height="12"><use href="#i-doc"/></svg>1</div></div>
  <div class="tile" style="left:841px;top:479px"><div class="tile-head">Elektronikk</div><div class="tile-row"><svg width="12" height="12"><use href="#i-cal"/></svg>2013-03-08</div><div class="tile-row"><svg width="12" height="12"><use href="#i-cash"/></svg>100</div><div class="tile-row"><svg width="12" height="12"><use href="#i-doc"/></svg>1</div></div>
  <div class="tile" style="left:995px;top:479px"><div class="tile-head">Elektronikk</div><div class="tile-row"><svg width="12" height="12"><use href="#i-cal"/></svg>2013-03-08</div><div class="tile-row"><svg width="12" height="12"><use href="#i-cash"/></svg>100</div><div class="tile-row"><svg width="12" height="12"><use href="#i-doc"/></svg>1</div></div>
  <div class="tile selected" style="left:841px;top:599px"><div class="tile-head">Elektronikk</div><div class="tile-row"><svg width="12" height="12"><use href="#i-cal"/></svg>2013-03-08</div><div class="tile-row"><svg width="12" height="12"><use href="#i-cash"/></svg>100</div><div class="tile-row"><svg width="12" height="12"><use href="#i-doc"/></svg>1</div></div>
  <div class="tile" style="left:995px;top:599px"><div class="tile-head">Elektronikk</div><div class="tile-row"><svg width="12" height="12"><use href="#i-cal"/></svg>2013-03-08</div><div class="tile-row"><svg width="12" height="12"><use href="#i-cash"/></svg>100</div><div class="tile-row"><svg width="12" height="12"><use href="#i-doc"/></svg>1</div></div>
</div>
</body>
</html>
```